Special Flyer for cleaning service

Hi, I am in need of a cleaning flyer for my cleaning business.

I want the following on it. Based on the attachment as well. Use our logo, the cartoon lady from attachment.

Only $69
Limited Time Only!

Vacuuming of all floors
Washing of hard floors
Furniture, skirtings and window sill dusting
Bins emptied
Kitchen benches, sinks, taps, stove top, microwave inside and out cleaned
Bathroom/Toilets thoroughly cleaned and sanitized including floors, sinks, taps, basins and shower.

Terms & Conditions
Maximum 3 bedrooms/2 bathrooms only/each additional room $10 extra
Maximum 3 hours labour
Limit one coupon per household

Coupon added to flyer - extra bonus coupon get $10 off price , use this flyer as reference

I want we accept lumo/paybridgex symbol
I want a fully insured symbol
turo symbol (attached in files)

Must be print ready A5
I'd like to keep logos/colour schemes from original flyer but want a real cleaning photo in it . But open to new ideas and want this flyer to be different to original

correct sizing to print online (direct from site)
Final flyer size:
A5 - 148mm x 210mm after trimming

Document size:
A5 - 158mm x 220mm (5mm bleed)

Do not include crop or trim marks in your artwork
A5 - 138mm x 200mm (5mm internal bleed)
Keep important information in this area

```html
<!DOCTYPE html>
<html lang="en">
<head>
<meta charset="utf-8">
<title>Coral Coast Cleaning Services – Flyer</title>
<link href="https://fonts.googleapis.com/css2?family=Lato:wght@400;700;900&family=Oswald:wght@600;700&display=swap" rel="stylesheet">
<style>
  :root {
    --blue: #1d9fc3;
    --blue-deep: #1689ab;
    --orange: #f8a21c;
    --white: #ffffff;
    --ink: #3a3a3a;
    --navy: #1d3f6e;
    --logo-teal: #2b7e9a;
    --badge: #2f3a38;
    --stage: #e8ebee;
  }
  * { box-sizing: border-box; margin: 0; padding: 0; }
  html, body { width: 905px; height: 1200px; overflow: hidden; }
  body { background: var(--stage); font-family: "Lato", Arial, sans-serif; }

  .flyer {
    position: absolute; left: 21px; top: 0;
    width: 863px; height: 1200px;
    background: var(--blue); overflow: hidden;
  }
  .flyer__shapes { position: absolute; inset: 0; }

  .brand {
    position: absolute; left: 75px; top: 88px; width: 310px;
    color: var(--logo-teal); font-weight: 900; font-size: 27px;
    line-height: 1.15; letter-spacing: 0.5px; text-transform: uppercase;
  }
  .badge {
    position: absolute; left: 427px; top: 79px;
    width: 104px; height: 104px; border-radius: 50%; background: var(--badge);
  }
  .illustration {
    position: absolute; left: 549px; top: 86px; width: 282px; height: 506px;
    border-radius: 120px 120px 20px 20px;
    background: linear-gradient(180deg, #f7a640 0%, #f3c7a6 35%, #76c9d6 70%, #f08a24 100%);
    opacity: 0.9;
  }

  .offer { position: absolute; left: 75px; top: 262px; color: var(--white); }
  .offer__price {
    font-family: "Oswald", Impact, sans-serif; font-weight: 700;
    font-size: 118px; line-height: 1; letter-spacing: -1px;
  }
  .offer__price span { color: var(--orange); }
  .offer__limit { font-weight: 700; font-size: 40px; line-height: 1; margin-top: 10px; }

  .service { position: absolute; left: 75px; top: 524px; width: 330px; }
  .service__title { color: var(--blue-deep); font-weight: 900; font-size: 28px; white-space: nowrap; }
  .service__freq { color: var(--orange); font-size: 21px; margin-top: 6px; white-space: nowrap; }
  .service__freq b { font-weight: 400; font-size: 12px; vertical-align: middle; color: var(--blue); margin: 0 4px; }

  .checklist { list-style: none; margin-top: 16px; width: 290px; }
  .checklist li {
    position: relative; padding-left: 30px; margin-bottom: 16px;
    color: var(--ink); font-weight: 700; font-size: 19px; line-height: 1.08;
  }
  .checklist li::before {
    content: ""; position: absolute; left: 0; top: 2px;
    width: 18px; height: 18px; border-radius: 50%; background: var(--orange);
  }
  .checklist li::after {
    content: ""; position: absolute; left: 6px; top: 5px;
    width: 5px; height: 9px; border: solid var(--white);
    border-width: 0 2px 2px 0; transform: rotate(45deg);
  }

  .coupon__tag {
    position: absolute; display: flex; align-items: center; justify-content: center;
    color: var(--white); white-space: nowrap;
  }
  .coupon__tag--top {
    left: 376px; top: 630px; width: 320px; height: 60px; background: var(--blue);
    font-size: 22px; font-weight: 700; align-items: flex-start; padding-top: 12px;
  }
  .coupon__tag--main {
    left: 412px; top: 680px; width: 400px; height: 88px; background: var(--orange);
    font-family: "Oswald", Impact, sans-serif; font-weight: 700; font-size: 46px;
  }
  .coupon__tag--ref { left: 517px; top: 766px; width: 314px; height: 55px; background: var(--blue); font-size: 17px; font-weight: 700; }

  .terms { position: absolute; left: 463px; top: 870px; width: 300px; }
  .terms__title {
    color: var(--orange); font-weight: 900; font-size: 20px;
    padding-bottom: 4px; border-bottom: 2px solid var(--orange); display: inline-block;
  }
  .terms__list { list-style: none; margin-top: 10px; }
  .terms__list li {
    position: relative; padding-left: 16px; margin-bottom: 8px;
    color: var(--ink); font-weight: 700; font-size: 17px; line-height: 1.2;
  }
  .terms__list li::before {
    content: ""; position: absolute; left: 0; top: 7px;
    width: 7px; height: 7px; border-radius: 50%; background: var(--orange);
  }

  .booking { position: absolute; left: 75px; top: 1032px; color: var(--white); }
  .booking__icon {
    position: absolute; left: 0; top: 8px; width: 58px; height: 58px;
    border-radius: 50%; background: var(--orange);
  }
  .booking__text { margin-left: 83px; }
  .booking__label { font-size: 22px; letter-spacing: 0.5px; }
  .booking__phone { font-weight: 900; font-size: 38px; line-height: 1.1; }
  .booking__social { margin-top: 14px; margin-left: 83px; font-size: 19px; display: flex; align-items: center; gap: 10px; }
  .booking__social i { width: 16px; height: 16px; background: var(--white); display: inline-block; }

  .payments { position: absolute; left: 517px; top: 1096px; display: flex; gap: 30px; }
  .payments__name { color: var(--navy); font-weight: 900; font-size: 26px; }
</style>
</head>
<body>
  <main class="flyer">
    <svg class="flyer__shapes" width="863" height="1200" viewBox="0 0 863 1200" aria-hidden="true">
      <path fill="var(--orange)" d="M0,0 H726 C610,170 320,262 0,262 Z"/>
      <path fill="var(--white)" d="M0,0 H671 C560,150 300,238 0,245 Z"/>
      <g fill="var(--orange)">
        <path transform="translate(0,-13)" d="M0,502 C150,465 330,460 500,520 C650,570 790,620 863,669 V1200 H470 C430,1010 300,945 0,965 Z"/>
        <path transform="translate(14,13)" d="M0,502 C150,465 330,460 500,520 C650,570 790,620 863,669 V1200 H470 C430,1010 300,945 0,965 Z"/>
      </g>
      <path fill="var(--white)" d="M0,502 C150,465 330,460 500,520 C650,570 790,620 863,669 V1200 H470 C430,1010 300,945 0,965 Z"/>
    </svg>

    <div class="brand">Coral Coast<br>Cleaning Services</div>
    <div class="badge" role="img" aria-label="Certification badge"></div>
    <div class="illustration" role="img" aria-label="Cartoon cleaning lady in orange apron holding a mop beside a bucket"></div>

    <section class="offer">
      <h1 class="offer__price">ONLY <span>$69</span></h1>
      <p class="offer__limit">LIMITED TIME ONLY!</p>
    </section>

    <section class="service">
      <h2 class="service__title">REGULAR CLEANING SERVICE</h2>
      <p class="service__freq">One-Time<b>●</b>Weekly<b>●</b>Fortnightly<b>●</b>Monthly</p>
      <ul class="checklist">
        <li>Vacuuming of all floors</li>
        <li>Washing of hard floors</li>
        <li>Furniture, skirtings and window sill dusting</li>
        <li>Bins emptied</li>
        <li>Kitchen benches, sinks, taps, stove top, microwave inside and out cleaned</li>
        <li>Bathroom/Toilets thoroughly cleaned and sanitized including floors, sinks, taps, basins and shower.</li>
      </ul>
    </section>

    <div class="coupon">
      <div class="coupon__tag coupon__tag--top">EXTRA BONUS COUPON</div>
      <div class="coupon__tag coupon__tag--main">GET $10 OFF PRICE</div>
      <div class="coupon__tag coupon__tag--ref">USE THIS FLYER AS REFERENCE</div>
    </div>

    <section class="terms">
      <h3 class="terms__title">TERMS &amp; CONDITIONS</h3>
      <ul class="terms__list">
        <li>Maximum 3 bedrooms/2 bathrooms only/each additional room $10 extra</li>
        <li>Maximum 3 hours labour</li>
        <li>Limit one coupon per household</li>
      </ul>
    </section>

    <section class="booking">
      <div class="booking__icon">
        <svg width="58" height="58" viewBox="0 0 58 58" aria-hidden="true">
          <rect x="15" y="27" width="28" height="16" rx="3" fill="none" stroke="#fff" stroke-width="2.5"/>
          <path d="M13,24 C18,15 40,15 45,24 L41,28 L36,24 L22,24 L17,28 Z" fill="#fff"/>
          <circle cx="29" cy="35" r="4" fill="none" stroke="#fff" stroke-width="2"/>
        </svg>
      </div>
      <div class="booking__text">
        <p class="booking__label">BOOK NOW :</p>
        <p class="booking__phone">0491570110</p>
      </div>
      <p class="booking__social"><i></i>Find us on Linkora</p>
    </section>

    <div class="payments">
      <span class="payments__name">LUMO</span>
      <span class="payments__name">PayBridgeX</span>
    </div>
  </main>
</body>
</html>
```